Business Card, Stationary, & Folder for Mortgage Company
KLD Mortgage
Business Card, Stationary, & Folder for Mortgage Company - Real Estate
Creative Brief
Professional
Terrin Balk
Senior Loan Officer
4186 Orchard Crest Blvd, #209 Takoma Park, Maryland 20912
tbalk@kldmortgage-example.com
www.KLDMortgage-example.com
I would like to use the colors in the logo but would like to also add a touch of red. I also would like to use the symbols for the phone numbers, email, and website
KLDMortgage KLDMortgage
I am looking for just a touch of red in the design. The main design should match the colors of the logo. Please don't alter the logo.
PixelHarborLab PixelHarborLab

```html
<!DOCTYPE html>
<html lang="en">
<head>
<meta charset="utf-8">
<title>KLD Mortgage — Stationery Set</title>
<link rel="stylesheet" href="https://fonts.googleapis.com/css2?family=Open+Sans:wght@400;700&display=swap">
<style>
:root{
  --stage:#6b7893;
  --stage-edge:#5d6984;
  --paper:#ffffff;
  --brand-blue:#2b4ba0;
  --brand-red:#d8392f;
  --wave-gray:#8d8d8f;
  --ink:#333a45;
  --soft-ink:#7a808a;
}
*{margin:0;padding:0;box-sizing:border-box}
html,body{width:1200px;height:967px;overflow:hidden}
body{background:var(--stage);font-family:"Open Sans",Arial,sans-serif;color:var(--ink)}
.stage{position:relative;width:1200px;height:967px;border:10px solid var(--stage-edge)}
.sheet{position:absolute;background:var(--paper);box-shadow:2px 3px 6px rgba(0,0,0,.35);overflow:hidden}
.wave{position:absolute;left:0;bottom:0;width:100%;height:62%}
.brand{position:absolute;display:flex;align-items:center;gap:4px;color:var(--brand-blue);font-weight:700;white-space:nowrap}
.brand::before{content:"";border-radius:50%;background:var(--brand-blue);flex:none}
.brand.s{font-size:9px}.brand.s::before{width:12px;height:12px}
.brand.m{font-size:13px}.brand.m::before{width:18px;height:18px}
.brand.sleeve{left:0;right:0;justify-content:center;font-size:17px;gap:6px}
.brand.sleeve::before{width:24px;height:24px}
.brand.light{color:#fff}.brand.light::before{background:#fff}
.tiny{position:absolute;font-size:5px;line-height:1.4;color:var(--soft-ink)}
.tiny.dark{color:var(--ink)}
.caption{position:absolute;font-size:6px;color:#1d2330}
.gray-card{background:var(--wave-gray)}
.fax-title{position:absolute;left:16px;top:38px;font-size:26px;font-weight:700;color:#111}
.fax-grid{position:absolute;left:16px;right:16px;top:80px;display:grid;grid-template-columns:1fr 1fr;column-gap:14px;row-gap:6px}
.fax-grid span{font-size:6px;border-bottom:1px solid #999;padding-bottom:1px}
.fax-checks{position:absolute;left:16px;right:12px;top:138px;display:flex;gap:8px;font-size:5px}
.fax-checks span::before{content:"";display:inline-block;width:5px;height:5px;border:1px solid #555;margin-right:2px;vertical-align:middle}
.fax-lines{position:absolute;left:16px;right:16px;top:150px;border-top:1px solid #999}
</style>
</head>
<body>
<svg width="0" height="0" style="position:absolute">
  <defs>
    <symbol id="swoosh" viewBox="0 0 100 100" preserveAspectRatio="none">
      <path d="M0,62 C30,30 65,18 100,12 L100,100 L0,100Z" fill="#8d8d8f"/>
      <path d="M0,48 C25,22 55,10 100,6" fill="none" stroke="#2b4ba0" stroke-width="2" vector-effect="non-scaling-stroke"/>
      <path d="M0,58 C30,26 65,14 100,9" fill="none" stroke="#d8392f" stroke-width="2" vector-effect="non-scaling-stroke"/>
    </symbol>
  </defs>
</svg>

<main class="stage">
  <section class="sheet business-card" style="left:128px;top:47px;width:154px;height:92px">
    <div class="brand s" style="left:8px;top:7px">KLD Mortgage</div>
    <div class="tiny dark" style="right:8px;top:26px;text-align:right">Terrin Balk<br>Senior Loan Officer</div>
    <svg class="wave" style="height:50%"><use href="#swoosh"/></svg>
  </section>
  <section class="sheet business-card" style="left:128px;top:168px;width:154px;height:92px">
    <div class="brand m" style="left:30px;top:34px">KLD Mortgage</div>
  </section>
  <section class="sheet business-card gray-card" style="left:128px;top:285px;width:154px;height:92px">
    <div class="brand m light" style="left:30px;top:34px">KLD Mortgage</div>
  </section>

  <section class="sheet letterhead" style="left:317px;top:47px;width:254px;height:356px">
    <div class="brand m" style="left:10px;top:10px">KLD Mortgage</div>
    <svg class="wave" style="height:26%"><use href="#swoosh"/></svg>
    <div class="tiny" style="left:10px;bottom:30px;color:#fff">4186 Orchard Crest Blvd, #209 Takoma Park, MD 20912<br>www.KLDMortgage-example.com</div>
  </section>

  <section class="sheet note-card" style="left:604px;top:47px;width:99px;height:105px">
    <div class="brand s" style="left:6px;top:6px">KLD</div>
    <svg class="wave" style="height:40%"><use href="#swoosh"/></svg>
  </section>
  <section class="sheet note-card" style="left:604px;top:186px;width:99px;height:57px">
    <div class="brand s" style="left:6px;top:5px">KLD</div>
    <svg class="wave" style="height:50%"><use href="#swoosh"/></svg>
  </section>

  <section class="sheet comp-slip" style="left:604px;top:285px;width:209px;height:118px">
    <div class="brand s" style="left:8px;top:7px">KLD Mortgage</div>
    <svg class="wave" style="height:55%"><use href="#swoosh"/></svg>
    <div class="tiny" style="left:8px;bottom:6px;color:#fff">4186 Orchard Crest Blvd, #209 Takoma Park, MD 20912</div>
  </section>

  <section class="envelopes" style="position:absolute;left:847px;top:225px;width:232px;height:160px">
    <svg width="232" height="160" style="filter:drop-shadow(2px 3px 3px rgba(0,0,0,.35))">
      <rect x="0" y="0" width="225" height="80" fill="#fff"/>
      <polygon points="0,0 225,0 225,10 112,34 0,10" fill="#d8392f"/>
      <rect x="3" y="32" width="225" height="80" fill="#fff"/>
      <polygon points="3,32 228,32 228,42 115,66 3,42" fill="#2b4ba0"/>
      <rect x="6" y="64" width="225" height="80" fill="#fff"/>
      <polyline points="6,64 118,96 231,64" fill="none" stroke="#ccc"/>
    </svg>
    <div class="caption" style="left:80px;top:150px">Envelope Back</div>
  </section>

  <section class="folder" style="position:absolute;left:115px;top:440px;width:500px;height:390px">
    <svg width="500" height="370" style="filter:drop-shadow(2px 3px 4px rgba(0,0,0,.35))">
      <path d="M10,0 H470 V12 L482,20 V150 L472,158 V366 H10 Z" fill="#fff"/>
      <path d="M10,40 L18,40 L18,330 L10,330Z" fill="#2b4ba0"/>
      <path d="M470,12 L482,20 V150 L472,158 V300 L464,300 V12Z" fill="#d8392f"/>
      <path d="M10,285 C150,230 320,205 472,195 V366 H10Z" fill="#8d8d8f"/>
      <path d="M10,262 C140,215 300,192 472,184" fill="none" stroke="#2b4ba0" stroke-width="2"/>
      <path d="M10,275 C150,222 320,200 472,190" fill="none" stroke="#d8392f" stroke-width="2"/>
      <path d="M252,366 L278,292 L304,366Z" fill="#fff"/>
      <rect x="380" y="292" width="78" height="44" fill="#fff" stroke="#bbb"/>
    </svg>
    <div class="brand s" style="left:22px;top:12px">KLD Mortgage</div>
    <div class="tiny" style="left:30px;top:330px;color:#fff">4186 Orchard Crest Blvd, #209 Takoma Park, MD 20912<br>www.KLDMortgage-example.com</div>
    <div class="caption" style="left:205px;top:378px">Presentation Folder</div>
  </section>

  <svg class="disc" style="position:absolute;left:635px;top:442px;filter:drop-shadow(2px 3px 3px rgba(0,0,0,.35))" width="150" height="150" viewBox="0 0 150 150">
    <defs><clipPath id="disc-clip"><circle cx="75" cy="75" r="73"/></clipPath></defs>
    <circle cx="75" cy="75" r="73" fill="#fff"/>
    <path clip-path="url(#disc-clip)" d="M0,95 C40,70 100,62 150,60 V150 H0Z" fill="#8d8d8f"/>
    <path clip-path="url(#disc-clip)" d="M0,82 C40,60 100,52 150,50" fill="none" stroke="#2b4ba0" stroke-width="2"/>
    <path clip-path="url(#disc-clip)" d="M0,90 C40,66 100,57 150,55" fill="none" stroke="#d8392f" stroke-width="2"/>
    <circle cx="75" cy="75" r="14" fill="#6b7893"/>
    <circle cx="75" cy="40" r="7" fill="#2b4ba0"/>
  </svg>

  <section class="sheet disc-sleeve" style="left:620px;top:601px;width:178px;height:217px">
    <svg style="position:absolute;left:0;top:0" width="178" height="40"><path d="M50,0 A40,36 0 0 0 128,0Z" fill="#8d8d8f"/></svg>
    <div class="brand sleeve" style="top:96px">KLD Mortgage</div>
  </section>

  <section class="sheet fax-sheet" style="left:831px;top:486px;width:225px;height:298px">
    <div class="brand s" style="left:10px;top:10px">KLD Mortgage</div>
    <div class="fax-title">Fax</div>
    <div class="fax-grid">
      <span>To:</span><span>From:</span>
      <span>Fax:</span><span>Pages:</span>
      <span>Phone:</span><span>Date:</span>
      <span>Re:</span><span>CC:</span>
    </div>
    <div class="fax-checks"><span>Urgent</span><span>For Review</span><span>Please Comment</span><span>Please Reply</span></div>
    <div class="fax-lines"></div>
  </section>
</main>
</body>
</html>
```